Luxury Lifestyle Website - Blog and Product Showcasing

I am looking to create a simple, yet elegant website where I can post blog posts and feature products and brand partnerships for my company, Velour Hollis. I want a very elegant but not overly complex site. I like the look and feel of Harriet Osborne's site - I don't need for it to be that robust or sophisticated, but that is the aesthetic I am going for. I would like to include my primary logo at the top of the main page, and also incorporate my alternative logos throughout the site in strategic places.

Target Market(s)

Luxury Brands; 20s-60s year olds; women; high-end fashion and tastes

Industry/Entity Type

Luxury Lifestyle - Blogging - Product Showcasing

Coding

Coded - Design and coding required

Number of Pages Required

4 page

Font styles to use
Sans Serif
Script
Other font styles liked:
• Pinyon

Colors
00AB8E
00BBA5
67D7C9
C6EFE9
E9F9F6
59FF00
82FF00
B8FF75
E3FFCB
F4FFEA

Requirements
Must have
• Creative use of my various logos. PASTEL GREENS or a DEEP DARK GREEN. Nothing bright, very soft and elegant.
Nice to have
• Elegant script that is easy to read.
Should not have
• Bright colors or overly modern look or feel.

```html
<!DOCTYPE html>
<html lang="en">
<head>
<meta charset="utf-8">
<title>Velour Hollis — Luxury Lifestyle</title>
<link rel="stylesheet" href="https://fonts.googleapis.com/css2?family=Playfair+Display:ital,wght@0,400;1,400&family=Montserrat:wght@400;500;600&family=Cormorant+Garamond:wght@400;500&family=Pinyon+Script&display=swap">
<style>
:root{
  --ink:#1d1d24;
  --muted:#6b6b72;
  --rule:#bdbdc2;
  --teal:#00ab8e;
  --teal-soft:#67d7c9;
  --mint:#c6efe9;
  --blush:#faf4f2;
  --forest:#0e2a25;
  --white:#ffffff;
}
*{box-sizing:border-box;margin:0;padding:0}
html,body{width:1200px;height:5204px;overflow:hidden;background:var(--white)}
body{position:relative;font-family:"Montserrat",sans-serif;color:var(--ink)}
.abs{position:absolute}
.serif-i{font-family:"Playfair Display",serif;font-style:italic;font-weight:400}
.script{font-family:"Pinyon Script",cursive}
.caps{text-transform:uppercase;letter-spacing:1.5px;font-weight:500}
.btn{position:absolute;display:flex;align-items:center;justify-content:center;border:1px solid var(--ink);font-size:12px;text-transform:uppercase;letter-spacing:1.5px;font-weight:500;background:var(--white)}
.btn.solid{background:var(--teal);border-color:var(--teal);color:var(--white)}
.rule-h{position:absolute;height:1px;background:var(--rule)}
.rule-v{position:absolute;width:1px;background:var(--rule)}
.photo{position:absolute}
.brand{font-family:"Cormorant Garamond",serif;font-weight:500;letter-spacing:1px;text-align:center}

/* header */
.site-header{position:absolute;left:0;top:0;width:1200px;height:96px;background:var(--white)}
.menu-toggle{left:46px;top:22px;width:52px;height:52px;border:1px dashed #999;border-radius:50%}
.main-nav a{position:absolute;top:40px;font-size:12px;text-transform:uppercase;letter-spacing:1px;color:var(--ink);text-decoration:none;font-weight:500}
.header-brand{left:500px;top:56px;width:200px;font-size:20px;color:#555}
.brand-square{left:582px;top:12px;width:36px;height:36px;border:1px solid #888}
.enquire-pill{left:1002px;top:28px;width:150px;height:38px;border:1px solid var(--ink);border-radius:20px;font-size:12px;letter-spacing:1px;display:flex;align-items:center;padding-left:18px;font-weight:500}
.enquire-pill span{position:absolute;right:6px;top:5px;width:26px;height:26px;border:1px dashed #777;border-radius:50%}

/* hero */
.hero{left:0;top:96px;width:1200px;height:564px;background:linear-gradient(100deg,#3d3a3a 0%,#6a5a4e 30%,#c99d86 55%,#e8c3ac 70%,#544c48 100%)}
.hero-overlay{left:0;top:96px;width:1200px;height:564px;background:rgba(20,16,16,.3)}
.hero-overlay *{color:var(--white)}
.hero-top{top:22px;font-size:11px;letter-spacing:.5px}
.hero-kicker{top:180px;width:1200px;text-align:center;font-size:18px}
.hero-title{top:208px;width:1200px;text-align:center;font-family:"Playfair Display",serif;font-weight:400;font-size:50px;line-height:68px;letter-spacing:3px}
.hero-btn{left:510px;top:352px;width:178px;height:50px;border:1px solid rgba(255,255,255,.8);display:flex;align-items:center;justify-content:center;font-size:11px;letter-spacing:1.5px}
.hero-line{left:599px;top:402px;width:1px;height:150px;background:rgba(255,255,255,.6)}
.hero-rule{left:0;top:506px;width:1200px;height:1px;background:rgba(255,255,255,.4)}
.hero-nav a{position:absolute;top:530px;font-size:11px;letter-spacing:1.2px;text-decoration:none}

/* professionals */
.pro-brand{left:500px;top:712px;width:200px;font-size:22px;color:var(--ink)}
.section-title{width:1200px;text-align:center;font-size:48px;line-height:54px;color:var(--ink)}
.stat{width:178px;height:178px;border:2px dotted #aaa;border-radius:50%;text-align:center}
.stat svg{margin-top:30px}
.stat b{display:block;font-family:"Playfair Display",serif;font-style:italic;font-weight:400;font-size:34px;margin-top:2px}
.stat small{display:block;font-size:10px;color:#999;margin-top:2px}

/* panels */
.panel{background:var(--blush)}
.panel-title{text-align:center;font-size:46px;line-height:54px}
.panel-copy{text-align:center;font-size:12px;line-height:19px;color:#333}

/* products */
.band{left:0;top:1699px;width:1200px;height:420px;background:linear-gradient(180deg,#f1f1f1,#e3e3e3)}
.card-label{position:absolute;top:160px;width:100%;text-align:center;color:var(--white);font-size:16px}
.card-ring{position:absolute;left:50%;top:50%;width:140px;height:140px;margin:-70px 0 0 -70px;border:1px dashed rgba(255,255,255,.6);border-radius:50%}
.circle-arrow{position:absolute;width:34px;height:34px;border-radius:50%;display:flex;align-items:center;justify-content:center}

/* founder */
.founder-copy{font-family:"Cormorant Garamond",serif;font-size:21px;line-height:26px;color:var(--ink)}

/* testimonials */
.quote{position:absolute;top:3447px;width:325px;height:225px;text-align:center}
.stars{color:var(--teal);font-size:16px;letter-spacing:3px;margin-top:30px}
.quote p{font-size:12px;line-height:21px;color:#333;margin:14px 42px 0}
.quote .script{color:var(--teal);font-size:26px;margin-top:12px}

/* newsletter */
.field{position:absolute;height:24px;border-bottom:1px solid var(--rule);font-size:10px;color:#999;text-align:center}

/* footer */
.site-footer{left:0;top:4673px;width:1200px;height:531px;background:var(--forest);color:var(--white)}
.site-footer .rule{position:absolute;left:0;width:1200px;height:1px;background:rgba(198,239,233,.25)}
.foot-nav a{position:absolute;font-size:12px;letter-spacing:1px;text-decoration:none;color:var(--white);font-weight:500}
.social{position:absolute;top:456px;width:18px;height:18px;border-radius:50%;background:var(--mint)}
</style>
</head>
<body>

<header class="site-header">
  <div class="abs menu-toggle"><svg width="52" height="52"><path d="M16 20h20M16 26h16M16 32h10" stroke="#222" stroke-width="2"/></svg></div>
  <nav class="main-nav">
    <a style="left:238px">Home</a><a style="left:316px">About Us</a><a style="left:422px">Videos</a>
    <a style="left:726px">Lifestyle</a><a style="left:830px">Fashion</a><a style="left:928px">Beauty</a>
  </nav>
  <div class="abs brand-square"></div>
  <div class="abs brand header-brand">VELOUR HOLLIS</div>
  <div class="abs enquire-pill">ENQUIRE<span></span></div>
</header>

<section class="abs hero" role="img" aria-label="Photo of a woman in a voluminous blush ruffled gown on a sunlit veranda"></section>
<section class="abs hero-overlay">
  <div class="abs hero-top" style="left:88px">GBP</div>
  <div class="abs hero-top" style="left:492px">★ ★ ★ ★ ★ &nbsp;<u>CUSTOMER RATING</u></div>
  <div class="abs hero-top" style="left:826px">SPEAK TO OUR EXPERT &nbsp;&nbsp; ✆ &nbsp;<span style="font-family:'Playfair Display',serif;font-style:italic;font-size:13px">+44 (020) 7946 0321</span></div>
  <div class="abs hero-kicker serif-i">Welcome to Velour Hollis Luxury Lifestyle</div>
  <h1 class="abs hero-title">IT'S TIME TO LEVEL UP<br>HOW YOU SHOW UP!</h1>
  <div class="abs hero-btn">GET INSPIRED</div>
  <div class="abs hero-line"></div>
  <div class="abs hero-rule"></div>
  <nav class="hero-nav"><a style="left:394px">NEWS</a><a style="left:478px">REVIEWS</a><a style="left:584px">OUR OFFERS</a><a style="left:716px">CONTACT US</a></nav>
</section>

<section>
  <div class="abs brand pro-brand">VELOUR HOLLIS</div>
  <h2 class="abs section-title serif-i" style="top:796px">We Help Professionals<br>Worldwide</h2>
  <div class="rule-h" style="left:0;top:1007px;width:285px"></div>
  <div class="rule-h" style="left:915px;top:1007px;width:285px"></div>
  <div class="abs stat" style="left:309px;top:919px"><svg width="40" height="36"><circle cx="20" cy="12" r="7" fill="none" stroke="#00ab8e" stroke-width="2"/><path d="M6 34c2-10 26-10 28 0" fill="none" stroke="#00ab8e" stroke-width="2"/></svg><b>100%</b><small>Success Rate</small></div>
  <div class="abs stat" style="left:511px;top:919px"><svg width="44" height="36"><circle cx="22" cy="10" r="6" fill="none" stroke="#00ab8e" stroke-width="2"/><circle cx="10" cy="20" r="5" fill="none" stroke="#00ab8e" stroke-width="2"/><circle cx="34" cy="20" r="5" fill="none" stroke="#00ab8e" stroke-width="2"/><path d="M4 34h36" stroke="#00ab8e" stroke-width="2"/></svg><b>Ultimate</b><small>Customer Satisfaction</small></div>
  <div class="abs stat" style="left:711px;top:919px"><svg width="40" height="36"><circle cx="20" cy="18" r="15" fill="none" stroke="#00ab8e" stroke-width="2"/><path d="M5 18h30M20 3c-8 8-8 22 0 30M20 3c8 8 8 22 0 30" fill="none" stroke="#00ab8e" stroke-width="1.5"/></svg><b>Worldwide</b><small>Business</small></div>
</section>

<section>
  <div class="abs panel" style="left:365px;top:1147px;width:723px;height:501px"></div>
  <div class="photo" style="left:113px;top:1213px;width:577px;height:367px;background:linear-gradient(90deg,#d9c2ae,#ead9c8 60%,#c8a98e)" role="img" aria-label="Photo of two women in utility jumpsuits posing beside a staircase and a potted plant"></div>
  <h2 class="abs panel-title serif-i" style="left:700px;top:1240px;width:363px">We've been<br>Nominated</h2>
  <p class="abs panel-copy" style="left:720px;top:1367px;width:323px">Lorem ipsum dolor sit amet, consectetur adipiscing elit, sed do eiusmod tempor incididunt ut labore et dolore magna aliqua. Quis ipsum suspendisse ultrices gravida. Risus commodo viverra.</p>
  <div class="btn" style="left:791px;top:1469px;width:180px;height:54px">Vote for us</div>
</section>

<section>
  <div class="abs band"></div>
  <h2 class="abs section-title serif-i" style="top:1736px;font-size:40px">Find Your Luxury Products</h2>
  <p class="abs panel-copy" style="left:280px;top:1797px;width:640px">Lorem ipsum dolor sit amet, consectetur adipiscing elit, sed do eiusmod tempor incididunt ut labore et dolore magna aliqua. Quis ipsum suspendisse ultrices gravida. Risus commodo viverra.</p>
  <div class="rule-h" style="left:0;top:1861px;width:1200px;background:#999"></div>
  <div class="photo" style="left:48px;top:1882px;width:298px;height:336px;background:linear-gradient(160deg,#6c6a6a,#4b4a4c)" role="img" aria-label="Photo of a woman in a black dress seated on a sofa"><div class="card-ring"></div><div class="card-label serif-i">Luxury Lifestyle</div></div>
  <div class="photo" style="left:366px;top:1882px;width:298px;height:336px;background:linear-gradient(160deg,#2f3330,#7a6460 70%,#c79b92)" role="img" aria-label="Photo of a woman in a pink dress among plants"><div class="card-ring"></div><div class="card-label serif-i">Simple Acts</div></div>
  <div class="photo" style="left:682px;top:1882px;width:298px;height:336px;background:linear-gradient(160deg,#7b8a5c,#b59f83 60%,#d6c2aa)" role="img" aria-label="Photo of a woman in a flowing beige outfit among palms"><div class="card-ring"></div><div class="card-label serif-i">Latest Style</div></div>
  <div class="photo" style="left:1000px;top:1882px;width:200px;height:336px;background:linear-gradient(160deg,#a3543f,#8c8c8c 60%,#d9d9d9)" role="img" aria-label="Photo of a woman in a cardigan outfit on a brick street"><div class="card-label serif-i" style="left:60px;width:140px">Outfit</div></div>
  <div class="circle-arrow" style="left:48px;top:2033px;background:#ddd;color:#777">←</div>
  <div class="circle-arrow" style="left:1116px;top:2033px;background:var(--white);color:#222">→</div>
  <div class="rule-h" style="left:0;top:2283px;width:492px"></div>
  <div class="rule-h" style="left:690px;top:2283px;width:510px"></div>
  <div class="btn" style="left:510px;top:2256px;width:180px;height:54px">Discover more</div>
</section>

<section>
  <div class="rule-h" style="left:113px;top:2360px;width:975px;background:#999"></div>
  <div class="rule-h" style="left:113px;top:2728px;width:975px;background:#999"></div>
  <div class="rule-v" style="left:466px;top:2360px;height:368px;background:#999"></div>
  <div class="photo" style="left:113px;top:2380px;width:334px;height:328px;background:linear-gradient(160deg,#9c7a55,#c9a27c 50%,#a7c6c0)" role="img" aria-label="Portrait photo of the founder in a mint top"></div>
  <p class="abs founder-copy" style="left:528px;top:2408px;width:540px">Lorem ipsum dolor sit amet, consectetur adipiscing elit, sed do eiusmod tempor incididunt ut labore et dolore magna aliqua. Quis ipsum suspendisse ultrices gravida. Risus commodo viverra maecenas accumsan lacus vel facilisis.</p>
  <div class="abs script" style="left:528px;top:2528px;font-size:18px;color:var(--teal)">Elena Marsh</div>
  <div class="abs caps" style="left:532px;top:2557px;font-size:11px;color:#555">Founder</div>
  <div class="btn" style="left:528px;top:2609px;width:180px;height:54px">About us</div>
</section>

<section>
  <div class="abs panel" style="left:0;top:2778px;width:718px;height:342px"></div>
  <h2 class="abs serif-i" style="left:113px;top:2820px;font-size:40px">Get Inspired</h2>
  <div class="rule-h" style="left:348px;top:2847px;width:637px;background:#999"></div>
  <div class="abs" style="left:1020px;top:2836px;font-size:16px">←</div>
  <div class="circle-arrow" style="left:1054px;top:2830px;background:#f6e6e3;color:#c33">→</div>
  <div class="photo" style="left:113px;top:2896px;width:297px;height:334px;background:linear-gradient(160deg,#6f5a3b,#2c2a33 60%,#8a6d45)" role="img" aria-label="Photo of a woman in a dark polka-dot dress among dried grasses"></div>
  <div class="photo" style="left:430px;top:2896px;width:298px;height:334px;background:linear-gradient(180deg,#3d7fb3,#a8c8de 45%,#1f5e5a)" role="img" aria-label="Photo of a woman in a teal gown against a blue sky"></div>
  <div class="photo" style="left:747px;top:2896px;width:298px;height:334px;background:linear-gradient(160deg,#3a4650,#1c2128 60%,#3e4a52)" role="img" aria-label="Photo of a woman in a black dress by a dark door"></div>
  <div class="photo" style="left:1064px;top:2896px;width:136px;height:334px;background:linear-gradient(160deg,#a66b3e,#d9b06a)" role="img" aria-label="Photo of a woman in a yellow patterned dress"></div>
  <div class="btn" style="left:113px;top:3268px;width:180px;height:54px">View more</div>
  <div class="rule-h" style="left:305px;top:3295px;width:783px;background:#999"></div>
</section>

<section>
  <h2 class="abs section-title serif-i" style="top:3364px;font-size:40px">From Our Clients</h2>
  <div class="rule-h" style="left:113px;top:3392px;width:310px;background:#999"></div>
  <div class="rule-h" style="left:773px;top:3392px;width:315px;background:#999"></div>
  <div class="rule-h" style="left:113px;top:3447px;width:975px;background:#999"></div>
  <div class="rule-h" style="left:113px;top:3672px;width:975px;background:#999"></div>
  <div class="rule-v" style="left:437px;top:3447px;height:225px;background:#999"></div>
  <div class="rule-v" style="left:762px;top:3447px;height:225px;background:#999"></div>
  <div class="quote" style="left:113px"><div class="stars">★★★★★</div><p>Lorem ipsum dolor sit amet, consectetur adipiscing elit, sed do eiusmod tempor incididunt ut labore et dolore magna aliqua. Quis ipsum suspendisse ultrices gravida. Risus</p><div class="script">Camila</div></div>
  <div class="quote" style="left:437px"><div class="stars">★★★★★</div><p>Lorem ipsum dolor sit amet, consectetur adipiscing elit, sed do eiusmod tempor incididunt ut labore et dolore magna aliqua. Quis ipsum suspendisse ultrices gravida. Risus</p><div class="script">Camila</div></div>
  <div class="quote" style="left:762px"><div class="stars">★★★★★</div><p>Lorem ipsum dolor sit amet, consectetur adipiscing elit, sed do eiusmod tempor incididunt ut labore et dolore magna aliqua. Quis ipsum suspendisse ultrices gravida. Risus</p><div class="script">Camila</div></div>
  <div class="abs" style="left:570px;top:3716px;font-size:16px">←</div>
  <div class="circle-arrow" style="left:602px;top:3710px;background:#f6e6e3;color:#c33">→</div>
</section>

<section>
  <div class="abs panel" style="left:365px;top:3790px;width:723px;height:500px"></div>
  <div class="photo" style="left:113px;top:3858px;width:577px;height:370px;background:linear-gradient(120deg,#6d1f4f,#b04a86 40%,#e6d8d8 60%,#3b2a35)" role="img" aria-label="Photo of a stylish couple in sunglasses against magenta foliage"></div>
  <h2 class="abs panel-title serif-i" style="left:720px;top:3900px;width:323px;font-size:42px;line-height:48px">It's time to<br>Level Up</h2>
  <p class="abs panel-copy" style="left:720px;top:4006px;width:323px">Speak to one of our fashion style specialists</p>
  <div class="btn solid" style="left:791px;top:4053px;width:180px;height:54px">Enquire now</div>
  <div class="btn" style="left:791px;top:4125px;width:180px;height:54px">Call us</div>
</section>

<section>
  <div class="rule-v" style="left:437px;top:4342px;height:283px;background:#999"></div>
  <div class="rule-v" style="left:762px;top:4342px;height:283px;background:#999"></div>
  <div class="abs brand" style="left:437px;top:4340px;width:325px;font-size:18px;color:#555">Velour Hollis</div>
  <h2 class="abs section-title serif-i" style="left:437px;top:4378px;width:325px;font-size:40px">Join with Us</h2>
  <p class="abs panel-copy" style="left:437px;top:4440px;width:325px">The latest offers &amp; inspiration straight to your inbox.</p>
  <div class="field" style="left:447px;top:4470px;width:144px">First Name*</div>
  <div class="field" style="left:608px;top:4470px;width:144px">Last Name*</div>
  <div class="field" style="left:447px;top:4513px;width:305px">Email Address*</div>
  <div class="btn" style="left:527px;top:4568px;width:146px;height:42px">Subscribe</div>
</section>

<footer class="abs site-footer">
  <div class="abs" style="left:582px;top:42px;width:36px;height:36px;border:1px solid rgba(198,239,233,.7)"></div>
  <div class="abs brand" style="left:450px;top:92px;width:300px;font-size:22px">VELOUR HOLLIS</div>
  <div class="rule" style="top:165px"></div>
  <nav class="foot-nav">
    <a style="left:334px;top:202px">HOME</a><a style="left:414px;top:202px">ABOUT US</a><a style="left:520px;top:202px">VIDEOS</a><a style="left:606px;top:202px">LIFESTYLE</a><a style="left:712px;top:202px">FASHION</a><a style="left:810px;top:202px">BEAUTY</a>
    <a style="left:394px;top:248px">NEWS</a><a style="left:478px;top:248px">REVIEWS</a><a style="left:584px;top:248px">OUR OFFERS</a><a style="left:716px;top:248px">CONTACT US</a>
  </nav>
  <div class="rule" style="top:295px"></div>
  <div class="abs" style="left:300px;top:333px;width:330px;text-align:center;font-size:10px;letter-spacing:1px">CALL US</div>
  <div class="abs serif-i" style="left:300px;top:356px;width:330px;text-align:center;font-size:16px">+44 (020) 7946 0321</div>
  <div class="abs" style="left:600px;top:310px;width:1px;height:100px;background:rgba(198,239,233,.5)"></div>
  <div class="abs" style="left:600px;top:333px;width:306px;text-align:center;font-size:10px;letter-spacing:1px">EMAIL US</div>
  <div class="abs serif-i" style="left:600px;top:356px;width:306px;text-align:center;font-size:16px">hello@velourhollis.com</div>
  <div class="rule" style="top:430px"></div>
  <div class="social" style="left:541px" aria-label="Social link"></div>
  <div class="social" style="left:591px" aria-label="Social link"></div>
  <div class="social" style="left:641px" aria-label="Social link"></div>
  <div class="abs" style="left:0;top:500px;width:1200px;text-align:center;font-size:11px;letter-spacing:1px">©2023 VELOURHOLLIS. ALL RIGHTS RESERVED</div>
</footer>

</body>
</html>
```